KMR Info Brochure

We need a brochure design for a new not-for-profit organisation that is aimed at providing homeless people with a residence that also provides counselling and vocational training to assist them to find suitable employment at the end of the program.
PLEASE NOTE:
Brochure to be A4.
I know the brochure is quite long, it is really a booklet, but please note that it does not have to have a lot of work done on it, I just want it to look professional and the front cover and inside page to look good.
Also please leave about 2-3 pages at the end as I will be adding in some architect drawings.
Please add in a last page with Contact written at the bottom - we will fill that in later. So please ensure it is editable in PDF.
Thank you so much.
Cheers
Petra

```html
<!DOCTYPE html>
<html lang="en">
<head>
<meta charset="utf-8">
<title>KMR Info Brochure – Learning For Residents</title>
<link rel="stylesheet" href="https://fonts.googleapis.com/css2?family=Arimo:wght@400;700&display=swap">
<style>
  :root {
    --olive: #8e8a2f;
    --olive-dark: #6e6a1e;
    --olive-mid: #a29d3f;
    --panel: #c9c58a;
    --gold: #f1b52e;
    --paper: #ffffff;
    --backdrop: #e4e4e4;
    --text: #3a3a3a;
    --heading: #8a8a2a;
  }
  * { box-sizing: border-box; margin: 0; padding: 0; }
  html, body {
    width: 1200px; height: 847px; overflow: hidden;
    background: radial-gradient(ellipse at 50% 35%, #f4f4f4 0%, var(--backdrop) 70%, #cfcfcf 100%);
    font-family: "Arimo", Arial, sans-serif;
    color: var(--text);
  }
  .spread {
    position: absolute; left: 60px; top: 42px;
    width: 1080px; height: 764px;
    display: flex;
    box-shadow: 0 10px 30px rgba(0,0,0,.18);
  }
  .page {
    position: relative; width: 540px; height: 764px;
    background: var(--paper); overflow: hidden;
  }
  .page--left::after, .page--right::after {
    content: ""; position: absolute; top: 0; bottom: 0; width: 30px; pointer-events: none;
  }
  .page--left::after { right: 0; background: linear-gradient(to left, rgba(0,0,0,.07), transparent); }
  .page--right::after { left: 0; background: linear-gradient(to right, rgba(0,0,0,.08), transparent); }
  .band { position: absolute; left: 0; top: 0; width: 540px; height: 764px; }

  .brand {
    position: absolute; left: 34px; top: 96px;
    display: flex; align-items: center; gap: 7px;
  }
  .brand__mark { width: 22px; height: 22px; border-radius: 50%; background: var(--gold); }
  .brand__name { font-size: 22px; font-weight: 700; color: var(--gold); letter-spacing: .5px; }

  .section-title {
    position: absolute; left: 34px; top: 132px;
    font-size: 23px; font-weight: 700; color: var(--heading);
  }
  .section-intro {
    position: absolute; left: 34px; top: 163px; width: 470px;
    font-size: 10.5px; line-height: 1.3; color: #333;
  }
  .course-list {
    position: absolute; left: 40px; top: 222px;
    list-style: none;
  }
  .course-list li {
    font-size: 11px; font-weight: 700; color: #555;
    line-height: 18.4px; display: flex; align-items: center; gap: 8px;
  }
  .course-list li::before {
    content: ""; width: 8px; height: 8px; border-radius: 50%;
    background: var(--gold);
  }
  .photo { position: absolute; left: 262px; width: 240px; }
  .photo--garden { top: 214px; height: 112px; background: linear-gradient(135deg, #6e5238 0%, #8d6a78 40%, #b89a48 70%, #5d7a3a 100%); }
  .photo--digital { top: 336px; height: 96px; background: linear-gradient(120deg, #3a6fa8 0%, #8fb4dc 45%, #23385e 100%); }
  .photo--reception { top: 442px; height: 130px; background: linear-gradient(135deg, #2b2520 0%, #6b5846 50%, #3d3228 100%); }
</style>
</head>
<body>
<div class="spread">
  <section class="page page--left">
    <svg class="band" viewBox="0 0 540 764">
      <defs>
        <linearGradient id="oliveFade" x1="0" x2="1">
          <stop offset="0" stop-color="var(--olive-dark)"/>
          <stop offset=".5" stop-color="var(--olive)"/>
          <stop offset="1" stop-color="var(--olive-mid)"/>
        </linearGradient>
        <clipPath id="footerWave">
          <path d="M0 716 Q330 702 540 636 V764 H0 Z"/>
        </clipPath>
      </defs>
      <g aria-hidden="true">
        <path d="M0 0 H540 V40 Q300 98 0 62 Z" fill="url(#oliveFade)"/>
        <path d="M0 70 Q300 104 540 50" fill="none" stroke="var(--gold)" stroke-width="3"/>
        <path d="M0 716 Q330 702 540 636 V764 H0 Z" fill="url(#oliveFade)"/>
      </g>
      <g clip-path="url(#footerWave)" role="img" aria-label="Decorative striped panel in light olive tones">
        <rect x="300" y="600" width="240" height="164" fill="var(--panel)"/>
      </g>
      <g aria-hidden="true">
        <path d="M0 708 Q330 694 540 628" fill="none" stroke="var(--gold)" stroke-width="3"/>
        <path d="M0 738 Q280 728 540 708 V764 H0 Z" fill="url(#oliveFade)"/>
        <path d="M0 734 Q280 724 540 704" fill="none" stroke="var(--paper)" stroke-width="4"/>
        <path d="M0 740 Q280 730 540 710" fill="none" stroke="var(--gold)" stroke-width="2.5"/>
      </g>
    </svg>

    <div class="brand">
      <span class="brand__mark"></span>
      <span class="brand__name">KMR</span>
    </div>

    <h1 class="section-title">Attachment 2: Learning For Residents</h1>
    <p class="section-intro">Below is a summary of the types of vocational training that will be available for Residents. Case Workers will also assist the Residents to find work experience during the learning phase of their Program and employment upon completion of their Program.</p>

    <ul class="course-list">
      <li>Accounting &amp; Finance</li>
      <li>Administration</li>
      <li>Animal Care</li>
      <li>Beauty</li>
      <li>Business</li>
      <li>Community and Aged Care</li>
      <li>Counselling</li>
      <li>Design</li>
      <li>Editing &amp; Proofreading</li>
      <li>Education and Childcare</li>
      <li>Health</li>
      <li>Horticulture &amp; Gardening</li>
      <li>Human Resources</li>
      <li>Information Technology</li>
      <li>Journalism</li>
      <li>Management</li>
      <li>Mechanics</li>
      <li>Natural Therapies</li>
      <li>Photography</li>
      <li>Tourism &amp; Hospitality</li>
      <li>Writing &amp; Communication</li>
    </ul>

    <div class="photo photo--garden" role="img" aria-label="Photo of hands potting colourful flowers in a garden"></div>
    <div class="photo photo--digital" role="img" aria-label="Photo of a businessman touching a digital interface"></div>
    <div class="photo photo--reception" role="img" aria-label="Photo of a hotel receptionist on the phone at a front desk"></div>
  </section>

  <section class="page page--right">
    <svg class="band" viewBox="0 0 540 764">
      <defs>
        <linearGradient id="oliveFadeR" x1="0" x2="1">
          <stop offset="0" stop-color="var(--olive-mid)"/>
          <stop offset=".5" stop-color="var(--olive)"/>
          <stop offset="1" stop-color="var(--olive-dark)"/>
        </linearGradient>
        <clipPath id="headerWave">
          <path d="M0 0 H540 V28 Q260 32 0 96 Z"/>
        </clipPath>
      </defs>
      <g aria-hidden="true">
        <path d="M0 0 H540 V28 Q260 32 0 96 Z" fill="url(#oliveFadeR)"/>
      </g>
      <g clip-path="url(#headerWave)" role="img" aria-label="Decorative striped panel in light olive tones">
        <rect x="0" y="0" width="120" height="100" fill="var(--panel)"/>
      </g>
      <g aria-hidden="true">
        <path d="M0 104 Q260 38 540 34" fill="none" stroke="var(--gold)" stroke-width="3"/>
        <path d="M0 700 Q300 696 540 650 V764 H0 Z" fill="url(#oliveFadeR)"/>
        <path d="M0 690 Q300 686 540 638" fill="none" stroke="var(--gold)" stroke-width="3"/>
        <path d="M0 706 Q300 703 540 660" fill="none" stroke="#f3cf78" stroke-width="2"/>
      </g>
    </svg>
  </section>
</div>
</body>
</html>
```